Modern Billboard Ad for Criminal Defense Firm

10.5 x 36 We're looking for something to set us apart from the local competition. Looking for sleek and modern. We're a mid-sized firm in a small market city. We want to give the artist room to be creative on this one.
Thanks

Target Market(s)

Adult clients who have been charged with a crime/DWI

Industry/Entity Type

legal

Font styles to use
Serif
Sans Serif

Requirements
Must have
• Needs to have the firm name in large lettering. Law Offices of Marcus T Whitfield. “PLLC” does not have to be included. Phone number of (555) 384-1927 should be included but not the main focus.
Nice to have
• A call to action or something similar. “Don’t go it alone, call today.”, “ Arrested?”

```html
<!DOCTYPE html>
<html lang="en">
<head>
<meta charset="utf-8">
<title>Law Offices of Marcus T Whitfield — Billboard</title>
<link href="https://fonts.googleapis.com/css2?family=Anton&family=Barlow+Condensed:wght@700&family=Poppins:wght@400;500;700&family=Roboto+Slab:wght@800&display=swap" rel="stylesheet">
<style>
  :root {
    --page: #ffffff;
    --slate: #2d3d4f;
    --navy: #0a1535;
    --royal: #1742a8;
    --ribbon: #03a9ec;
    --badge: #231f20;
    --ink-light: #ffffff;
    --photo-light: #8fa6c4;
    --photo-dark: #3d5475;
  }
  html, body {
    margin: 0;
    width: 1200px;
    height: 848px;
    overflow: hidden;
    background: var(--page);
  }
  .canvas {
    position: relative;
    width: 1200px;
    height: 848px;
  }
  .billboard {
    position: absolute;
    left: 0;
    top: 0;
  }
  .eyebrow {
    font-family: "Poppins", sans-serif;
    font-weight: 500;
    font-size: 13px;
    letter-spacing: 4.2px;
    fill: var(--ink-light);
  }
  .firm-name {
    font-family: "Barlow Condensed", sans-serif;
    font-weight: 700;
    font-size: 37px;
    fill: var(--ink-light);
  }
  .ribbon-label {
    font-family: "Roboto Slab", serif;
    font-weight: 800;
    font-size: 14px;
    fill: var(--ink-light);
  }
  .headline {
    font-family: "Anton", sans-serif;
    font-size: 78px;
    fill: var(--ink-light);
  }
  .question {
    font-family: "Poppins", sans-serif;
    font-weight: 700;
    font-size: 104px;
    fill: var(--ink-light);
  }
  .tagline {
    font-family: "Poppins", sans-serif;
    font-weight: 500;
    font-size: 11.5px;
    letter-spacing: 4.4px;
    fill: var(--ink-light);
  }
  .phone {
    font-family: "Poppins", sans-serif;
    font-weight: 700;
    font-size: 22px;
    fill: var(--ink-light);
  }
</style>
</head>
<body>
<div class="canvas">
  <svg class="billboard" width="1200" height="848" viewBox="0 0 1200 848" xmlns="http://www.w3.org/2000/svg">
    <defs>
      <linearGradient id="portraitTone" x1="0" y1="0" x2="1" y2="1">
        <stop offset="0" stop-color="var(--photo-light)"/>
        <stop offset="1" stop-color="var(--photo-dark)"/>
      </linearGradient>
      <linearGradient id="statueTone" x1="0" y1="0" x2="1" y2="0">
        <stop offset="0" stop-color="#2d3d4f"/>
        <stop offset="0.5" stop-color="#2c4a80"/>
        <stop offset="1" stop-color="#8fd6e6"/>
      </linearGradient>
      <linearGradient id="bandTone" x1="0" y1="0" x2="1" y2="0">
        <stop offset="0" stop-color="var(--navy)"/>
        <stop offset="0.7" stop-color="var(--navy)"/>
        <stop offset="1" stop-color="#0c3a8c"/>
      </linearGradient>
    </defs>

    <!-- portrait panel -->
    <rect class="portrait" x="113" y="278" width="290" height="277" fill="url(#portraitTone)" role="img" aria-label="Portrait photo of the attorney in a suit against a wooden wall"/>
    <rect class="name-band" x="113" y="473" width="290" height="82" fill="var(--royal)" opacity="0.92"/>
    <text class="eyebrow" x="128" y="503">LAW OFFICES OF</text>
    <text class="firm-name" x="128" y="535" textLength="262" lengthAdjust="spacingAndGlyphs">MARCUS T WHITFIELD</text>

    <!-- message panel -->
    <rect class="message-panel" x="482" y="278" width="583" height="195" fill="var(--slate)"/>
    <rect class="statue" x="821" y="278" width="244" height="277" fill="url(#statueTone)" role="img" aria-label="Photo of a bronze Lady Justice statue holding scales"/>
    <rect class="cta-band" x="403" y="473" width="662" height="82" fill="url(#bandTone)" opacity="0.95"/>

    <!-- stamp headline -->
    <g class="stamp" transform="rotate(-5.5 662 384)">
      <rect x="497" y="328" width="332" height="112" rx="16" fill="none" stroke="var(--ink-light)" stroke-width="7"/>
      <text class="headline" x="663" y="421" text-anchor="middle" textLength="306" lengthAdjust="spacingAndGlyphs">ARRESTED</text>
    </g>
    <text class="question" x="849" y="408">?</text>

    <!-- award ribbon -->
    <polygon class="ribbon" points="403,276 482,276 482,534 442,521 403,534" fill="var(--ribbon)"/>
    <rect class="award-badge" x="405" y="376" width="76" height="94" fill="var(--badge)" role="img" aria-label="Community choice award badge"/>
    <text class="ribbon-label" x="442.5" y="486" text-anchor="middle">WINNER</text>

    <!-- call to action -->
    <text class="tagline" x="513" y="521">DON’T GO IT ALONE.&#160;&#160;CALL TODAY</text>
    <text class="phone" x="852" y="522">(555) 384-1927</text>
  </svg>
</div>
</body>
</html>
```